Halvorsen Chiropractic we would like to design a trifold brochure that highlights our services

We need a Trifold created for our Chiropractic offices that highlights our services and treatments that we offer giving patients a better quality of life . Areas to highlight
conditions can be found on our websites and specialties .www.halvorsenchiropractic.example
our doctors have over 20 years experience in this field .
they have worked with the Ridgeback Falcons and Dr. Ned Halvorsen is the Marlowe Crest university basketball teams main chiropractor.

Target Market(s)

children to elderly

Font styles to use
Serif

Colors
00a990
0255a3

Requirements
Must have
• logo
• contact info
• pics of doctors
• bios of doctors
• location
• services provided
Nice to have
• none
Should not have
• do not use picture on website of staff we have all new staff in office

```html
<!DOCTYPE html>
<html lang="en">
<head>
<meta charset="utf-8">
<title>Halvorsen Chiropractic – Trifold Brochure</title>
<link rel="stylesheet" href="https://fonts.googleapis.com/css2?family=Anton&family=Montserrat:wght@400;700&family=Tinos:ital,wght@0,400;0,700;1,400;1,700&display=swap">
<style>
  :root {
    --teal: #00a990;
    --teal-deep: #0a9c86;
    --blue: #0255a3;
    --blue-soft: #7fb0cf;
    --ink: #1a1a1a;
    --slate: #2f4a4a;
    --green: #5cb531;
    --paper: #ffffff;
    --backdrop: #e4e6e8;
  }
  * { box-sizing: border-box; margin: 0; padding: 0; }
  html, body { width: 1200px; height: 800px; overflow: hidden; background: var(--backdrop); }
  .brochure {
    position: absolute; left: 45px; top: 30px;
    width: 1110px; height: 740px;
    display: flex;
    box-shadow: 0 10px 30px rgba(0,0,0,.18);
  }
  .panel { position: relative; width: 370px; height: 740px; background: var(--paper); overflow: hidden; }
  .panel + .panel { border-left: 1px solid rgba(0,0,0,.06); }
  .panel-art { position: absolute; inset: 0; width: 100%; height: 100%; }
  .band-top { position: absolute; left: 0; top: 0; width: 100%; height: 26px; background: var(--blue); }

  /* Services panel */
  .services-header { position: absolute; left: 34px; top: 52px; display: flex; align-items: center; gap: 10px; }
  .services-icon { width: 30px; height: 30px; background: var(--teal); border-radius: 3px; }
  .services-title {
    font-family: "Tinos", serif; font-style: italic; font-weight: 700;
    font-size: 17px; color: var(--ink); text-transform: uppercase; letter-spacing: .2px;
  }
  .services-list {
    position: absolute; left: 38px; top: 112px; list-style: none;
    font-family: "Tinos", serif; font-style: italic; font-size: 15px; color: var(--ink);
  }
  .services-list li { display: flex; align-items: center; gap: 10px; height: 23.5px; }
  .services-list svg { flex: none; }

  /* Doctor panel */
  .doctor-photo {
    position: absolute; left: 90px; top: 60px; width: 190px; height: 200px;
    border: 6px solid #f2f2f2; border-radius: 8px;
    background: linear-gradient(160deg, #d9d2cb 0%, #b9a99b 55%, #3b3a3a 100%);
  }
  .doctor-name {
    position: absolute; left: 0; top: 300px; width: 100%; text-align: center;
    font-family: "Montserrat", sans-serif; font-weight: 700; font-size: 34px;
    line-height: 38px; letter-spacing: 3px; color: var(--slate);
  }
  .doctor-rule { position: absolute; left: 110px; top: 384px; width: 150px; height: 1px; background: var(--slate); }
  .doctor-role {
    position: absolute; left: 0; top: 393px; width: 100%; text-align: center;
    font-family: "Montserrat", sans-serif; font-size: 13px; letter-spacing: 1px; color: var(--paper);
  }
  .contact { position: absolute; left: 36px; display: flex; align-items: flex-start; gap: 14px; font-family: "Tinos", serif; color: var(--ink); }
  .contact-icon { width: 44px; height: 40px; background: var(--blue); display: grid; place-items: center; flex: none; }
  .contact-phone { top: 510px; font-size: 30px; align-items: center; }
  .contact-address { top: 580px; font-size: 21px; line-height: 26px; }

  /* Cover panel */
  .brand { position: absolute; left: 0; top: 62px; width: 100%; display: flex; justify-content: center; align-items: center; gap: 12px; }
  .brand-mark { width: 18px; height: 18px; border-radius: 50%; background: var(--blue); }
  .brand-name { font-family: "Tinos", serif; font-weight: 700; font-size: 27px; color: var(--blue); }
  .headline {
    position: absolute; left: 0; top: 176px; width: 100%; text-align: center;
    font-family: "Anton", sans-serif; color: var(--paper); text-transform: none;
  }
  .headline-line1 { display: block; font-size: 40px; line-height: 50px; }
  .headline-line2 { display: block; font-size: 50px; line-height: 62px; text-transform: uppercase; }
  .headline-line3 { display: block; font-size: 62px; line-height: 74px; text-transform: uppercase; letter-spacing: 1px; }
</style>
</head>
<body>
<main class="brochure">

  <!-- Services panel -->
  <section class="panel panel-services">
    <svg class="panel-art" viewBox="0 0 370 740" aria-hidden="true">
      <rect x="0" y="0" width="370" height="26" fill="var(--blue)"/>
      <path d="M30 96 Q190 84 340 98 L340 103 Q190 90 30 101 Z" fill="var(--teal)"/>
      <rect x="0" y="664" width="370" height="14" fill="var(--blue-soft)"/>
      <rect x="0" y="678" width="370" height="62" fill="var(--blue)"/>
    </svg>
    <div class="services-header">
      <svg class="services-icon" viewBox="0 0 30 30" aria-hidden="true">
        <rect width="30" height="30" rx="3" fill="#00a990"/>
        <rect x="8" y="7" width="14" height="17" fill="none" stroke="#fff" stroke-width="1.6"/>
        <line x1="11" y1="12" x2="19" y2="12" stroke="#fff" stroke-width="1.4"/>
        <line x1="11" y1="16" x2="19" y2="16" stroke="#fff" stroke-width="1.4"/>
        <line x1="11" y1="20" x2="17" y2="20" stroke="#fff" stroke-width="1.4"/>
      </svg>
      <h2 class="services-title">Services and Treatments</h2>
    </div>
    <ul class="services-list">
      <li><svg width="11" height="10" viewBox="0 0 11 10"><path d="M1 5 L4 8 L10 1" fill="none" stroke="#0255a3" stroke-width="1.8"/></svg>Chiropractic Manipulation and Adjustments</li>
      <li><svg width="11" height="10" viewBox="0 0 11 10"><path d="M1 5 L4 8 L10 1" fill="none" stroke="#0255a3" stroke-width="1.8"/></svg>Spinal Decompression</li>
      <li><svg width="11" height="10" viewBox="0 0 11 10"><path d="M1 5 L4 8 L10 1" fill="none" stroke="#0255a3" stroke-width="1.8"/></svg>DOT Physicals</li>
      <li><svg width="11" height="10" viewBox="0 0 11 10"><path d="M1 5 L4 8 L10 1" fill="none" stroke="#0255a3" stroke-width="1.8"/></svg>Dry Needling</li>
      <li><svg width="11" height="10" viewBox="0 0 11 10"><path d="M1 5 L4 8 L10 1" fill="none" stroke="#0255a3" stroke-width="1.8"/></svg>Pain Management Therapy and Rehabilitation</li>
      <li><svg width="11" height="10" viewBox="0 0 11 10"><path d="M1 5 L4 8 L10 1" fill="none" stroke="#0255a3" stroke-width="1.8"/></svg>In Office X-Ray</li>
      <li><svg width="11" height="10" viewBox="0 0 11 10"><path d="M1 5 L4 8 L10 1" fill="none" stroke="#0255a3" stroke-width="1.8"/></svg>Orthopedic and Neurological Exams</li>
      <li><svg width="11" height="10" viewBox="0 0 11 10"><path d="M1 5 L4 8 L10 1" fill="none" stroke="#0255a3" stroke-width="1.8"/></svg>Flexibility Training</li>
      <li><svg width="11" height="10" viewBox="0 0 11 10"><path d="M1 5 L4 8 L10 1" fill="none" stroke="#0255a3" stroke-width="1.8"/></svg>Sensory-Motor and Balance Training</li>
      <li><svg width="11" height="10" viewBox="0 0 11 10"><path d="M1 5 L4 8 L10 1" fill="none" stroke="#0255a3" stroke-width="1.8"/></svg>Myo-facial Therapy by a licensed CTA</li>
      <li><svg width="11" height="10" viewBox="0 0 11 10"><path d="M1 5 L4 8 L10 1" fill="none" stroke="#0255a3" stroke-width="1.8"/></svg>Goal Oriented Care</li>
      <li><svg width="11" height="10" viewBox="0 0 11 10"><path d="M1 5 L4 8 L10 1" fill="none" stroke="#0255a3" stroke-width="1.8"/></svg>Corrective Exercises</li>
      <li><svg width="11" height="10" viewBox="0 0 11 10"><path d="M1 5 L4 8 L10 1" fill="none" stroke="#0255a3" stroke-width="1.8"/></svg>Nutritional Counseling</li>
      <li><svg width="11" height="10" viewBox="0 0 11 10"><path d="M1 5 L4 8 L10 1" fill="none" stroke="#0255a3" stroke-width="1.8"/></svg>Orthotics</li>
      <li><svg width="11" height="10" viewBox="0 0 11 10"><path d="M1 5 L4 8 L10 1" fill="none" stroke="#0255a3" stroke-width="1.8"/></svg>Spinal and Postural Screenings</li>
      <li><svg width="11" height="10" viewBox="0 0 11 10"><path d="M1 5 L4 8 L10 1" fill="none" stroke="#0255a3" stroke-width="1.8"/></svg>Lifestyle Advice</li>
      <li><svg width="11" height="10" viewBox="0 0 11 10"><path d="M1 5 L4 8 L10 1" fill="none" stroke="#0255a3" stroke-width="1.8"/></svg>Workplace and Community Workshops</li>
      <li><svg width="11" height="10" viewBox="0 0 11 10"><path d="M1 5 L4 8 L10 1" fill="none" stroke="#0255a3" stroke-width="1.8"/></svg>Personal Injury and Motor Vehicle Accidents</li>
      <li><svg width="11" height="10" viewBox="0 0 11 10"><path d="M1 5 L4 8 L10 1" fill="none" stroke="#0255a3" stroke-width="1.8"/></svg>Workmans Comp Cases</li>
    </ul>
  </section>

  <!-- Doctor panel -->
  <section class="panel panel-doctor">
    <svg class="panel-art" viewBox="0 0 370 740" aria-hidden="true">
      <rect x="0" y="0" width="370" height="26" fill="var(--blue)"/>
      <path d="M0 40 Q185 26 370 40 L370 440 Q185 400 0 440 Z" fill="var(--teal)"/>
      <path d="M0 34 Q185 20 370 34 L370 40 Q185 26 0 40 Z" fill="#fff"/>
      <path d="M0 660 Q185 690 370 660 L370 672 Q185 702 0 672 Z" fill="var(--teal)"/>
      <path d="M0 672 Q185 702 370 672 L370 740 L0 740 Z" fill="var(--blue)"/>
    </svg>
    <div class="doctor-photo" role="img" aria-label="Portrait photo of the doctor"></div>
    <h2 class="doctor-name">MIRA<br>LUND</h2>
    <div class="doctor-rule"></div>
    <p class="doctor-role">DOCTOR</p>
    <div class="contact contact-phone">
      <span class="contact-icon">
        <svg width="26" height="22" viewBox="0 0 26 22" aria-hidden="true"><path d="M3 8 Q13 0 23 8 L20 11 L17 8 L17 6 Q13 4 9 6 L9 8 L6 11 Z M8 12 L18 12 L21 20 L5 20 Z" fill="#fff"/><circle cx="13" cy="16" r="2.4" fill="#0255a3"/></svg>
      </span>
      <span>(555) 214-0388</span>
    </div>
    <div class="contact contact-address">
      <span class="contact-icon">
        <svg width="16" height="22" viewBox="0 0 16 22" aria-hidden="true"><path d="M8 1 A7 7 0 0 1 15 8 C15 13 8 21 8 21 C8 21 1 13 1 8 A7 7 0 0 1 8 1 Z" fill="#fff"/><circle cx="8" cy="8" r="2.6" fill="#0255a3"/></svg>
      </span>
      <span>48 Larchmont Way #12<br>Brookhaven, ST 00412</span>
    </div>
  </section>

  <!-- Cover panel -->
  <section class="panel panel-cover">
    <svg class="panel-art" viewBox="0 0 370 740" aria-hidden="true">
      <rect x="0" y="0" width="370" height="26" fill="var(--blue)"/>
      <path d="M0 180 Q185 140 370 165 L370 460 Q185 430 0 470 Z" fill="var(--teal)"/>
      <path d="M0 660 Q185 690 370 660 L370 672 Q185 702 0 672 Z" fill="var(--teal)"/>
      <path d="M0 672 Q185 702 370 672 L370 740 L0 740 Z" fill="var(--blue)"/>
    </svg>
    <div class="brand">
      <span class="brand-mark"></span>
      <span class="brand-name">Halvorsen Chiropractic</span>
    </div>
    <h1 class="headline">
      <span class="headline-line1">Chiropractic &amp;</span>
      <span class="headline-line2">Whole Body</span>
      <span class="headline-line3">Wellness</span>
    </h1>
    <svg class="panel-art" viewBox="0 0 370 740" role="img" aria-label="Photo of the clinic's doctors reviewing an x-ray">
      <defs>
        <linearGradient id="cover-photo-tone" x1="0" y1="0" x2="1" y2="1">
          <stop offset="0" stop-color="#e9eef2"/>
          <stop offset=".55" stop-color="#b9cfe0"/>
          <stop offset="1" stop-color="#dfe4e8"/>
        </linearGradient>
      </defs>
      <path d="M0 470 Q185 430 370 460 L370 650 Q185 680 0 650 Z" fill="url(#cover-photo-tone)"/>
    </svg>
  </section>

</main>
</body>
</html>
```